Lantern Cove Summer Camps Banner Ads

Seeking to create 6 banner ads (two variations of 3 banner sizes. 1) 250x250 2)468x60 3)120x600.
We are a Spanish and French immersion summer camp based in Chapel Hill, North Carolina. You can view our website at http://lanterncove-example.org
We've included our logo attached, colors should be reflective of branded colors in the logo.
Our target market is the South East, United State (FL, GA, NC, SC, TN, VA). Parents (focus on mothers) with kids from grades 1-12 (ages 5-17).
Our calls to action are to register/sign up for camps, and explore our website (Goal is clicks not views).
Language for ad: English.
Final design should be a fun, family-centric ad, which encapsulates the user and encourages them to learn more about Lantern Cove. Preferably, ad can be used ever-green for reuse in different seasons (does not contain date restrictions, for example ad should NOT contain "Join us for Summer Camp 2018").
Typical tag lines include: Friends, languages and a lot of fun! All the fun of a summer camp while totally immersed in the language and culture!
Target Market(s)

```html
<!DOCTYPE html>
<html lang="en">
<head>
<meta charset="utf-8">
<title>Lantern Cove Summer Camps – Banner Ads</title>
<link rel="stylesheet" href="https://fonts.googleapis.com/css2?family=Oswald:wght@400;500&family=Open+Sans:wght@400;600;700&display=swap">
<style>
  :root {
    --stage: #616161;
    --paper: #ffffff;
    --brand-blue: #3d78c4;
    --brand-teal: #12a389;
    --ink: #111111;
    --rule: #333333;
  }
  * { margin: 0; padding: 0; box-sizing: border-box; }
  html, body { width: 1200px; height: 1164px; overflow: hidden; background: var(--stage); }
  .canvas { position: relative; width: 1200px; height: 1164px; }

  .banner { position: absolute; background: var(--paper); overflow: hidden; }
  .banner svg.art { position: absolute; left: 0; top: 0; width: 100%; }

  .brand-name {
    position: absolute; color: var(--paper);
    font-family: "Open Sans", sans-serif; font-weight: 700; line-height: 1.05;
  }
  .headline {
    position: absolute; color: var(--brand-teal);
    font-family: "Oswald", sans-serif; font-weight: 500; line-height: 1.05; letter-spacing: -0.2px;
  }
  .subhead {
    position: absolute; color: var(--ink);
    font-family: "Oswald", sans-serif; font-weight: 400; line-height: 1.15;
  }
  .tagline {
    position: absolute; color: var(--ink);
    font-family: "Open Sans", sans-serif; font-weight: 400; line-height: 1.3;
  }
  .cta {
    position: absolute; display: flex; align-items: center; justify-content: center; gap: 8px;
    border: 2px solid var(--rule); border-radius: 4px; color: var(--ink);
    font-family: "Open Sans", sans-serif; font-weight: 700; letter-spacing: 2px;
  }
  .cta svg { display: block; }
  .site-url {
    position: absolute; color: var(--ink);
    font-family: "Open Sans", sans-serif; font-weight: 700; letter-spacing: 1.2px; text-align: center;
  }
  .divider { position: absolute; height: 2px; background: var(--rule); }

  /* Skyscraper 120x600 */
  .skyscraper { left: 98px; top: 84px; width: 194px; height: 971px; }
  .skyscraper .brand-name { left: 6px; top: 8px; font-size: 11px; }
  .skyscraper .headline { left: 0; width: 194px; top: 522px; font-size: 37px; text-align: center; }
  .skyscraper .subhead { left: 0; width: 194px; top: 606px; font-size: 28px; text-align: center; }
  .skyscraper .divider { left: 60px; width: 75px; top: 703px; }
  .skyscraper .tagline { left: 0; width: 194px; top: 743px; font-size: 17px; text-align: center; }
  .skyscraper .cta { left: 17px; top: 862px; width: 162px; height: 42px; font-size: 20px; }
  .skyscraper .site-url { left: 0; width: 194px; top: 930px; font-size: 11.5px; }

  /* Square 250x250 */
  .square { left: 391px; top: 84px; width: 405px; height: 405px; }
  .square .brand-name { left: 6px; top: 12px; font-size: 11px; }
  .square .headline { left: 18px; top: 215px; font-size: 35px; }
  .square .subhead { left: 19px; top: 252px; font-size: 23px; }
  .square .tagline { left: 19px; top: 300px; font-size: 17px; }
  .square .cta { left: 17px; top: 347px; width: 163px; height: 42px; font-size: 20px; }
  .square .site-url { left: 226px; top: 365px; font-size: 11.5px; }

  /* Leaderboard 468x60 */
  .leaderboard { left: 391px; top: 544px; width: 758px; height: 98px; }
  .leaderboard .brand-name { left: 4px; top: 80px; font-size: 8px; }
  .leaderboard .headline { left: 246px; top: 23px; font-size: 26px; }
  .leaderboard .subhead { left: 268px; top: 53px; font-size: 18px; }
  .leaderboard .tagline { left: 465px; width: 120px; top: 26px; font-size: 13px; font-weight: 600; line-height: 1.2; text-align: center; }
  .leaderboard .cta { left: 602px; top: 27px; width: 128px; height: 33px; font-size: 17px; gap: 6px; }
  .leaderboard .site-url { left: 602px; width: 128px; top: 66px; font-size: 10px; }
</style>
</head>
<body>
<main class="canvas">

  <section class="banner skyscraper" aria-label="Lantern Cove 120 by 600 banner">
    <svg class="art" viewBox="0 0 167 834" height="971" preserveAspectRatio="none">
      <defs>
        <linearGradient id="sky-photo" x1="0" y1="0" x2="0" y2="1">
          <stop offset="0" stop-color="#4f6a3a"/>
          <stop offset="0.3" stop-color="#b9b8a8"/>
          <stop offset="0.7" stop-color="#d9d6d2"/>
          <stop offset="1" stop-color="#6e6a62"/>
        </linearGradient>
      </defs>
      <polygon points="0,0 167,0 167,406 0,366" fill="url(#sky-photo)" role="img" aria-label="Photo of camp children in white shirts with a teacher in front of a camp sign"/>
      <polygon points="0,366 167,400 167,406 0,372" fill="var(--brand-blue)"/>
      <polygon points="0,0 104,0 0,58" fill="var(--brand-blue)"/>
    </svg>
    <div class="brand-name">Lantern<br>Cove</div>
    <h2 class="headline">LANGUAGE<br>IMMERSION</h2>
    <p class="subhead">Summer and<br>Break Camps</p>
    <div class="divider"></div>
    <p class="tagline">All the fun of a<br>“traditional”<br>summer camp</p>
    <div class="cta"><svg width="10" height="12" viewBox="0 0 10 12"><polygon points="0,0 10,6 0,12" fill="currentColor"/></svg>SIGN UP</div>
    <div class="site-url">lanterncove-example.org</div>
  </section>

  <section class="banner square" aria-label="Lantern Cove 250 by 250 banner">
    <svg class="art" viewBox="0 0 348 348" height="405" preserveAspectRatio="none">
      <defs>
        <linearGradient id="square-photo" x1="0" y1="0" x2="0" y2="1">
          <stop offset="0" stop-color="#c0608a"/>
          <stop offset="0.2" stop-color="#8a6e58"/>
          <stop offset="0.55" stop-color="#e2ddd6"/>
          <stop offset="1" stop-color="#7a5b3e"/>
        </linearGradient>
      </defs>
      <polygon points="0,0 348,0 348,200 0,108" fill="url(#square-photo)" role="img" aria-label="Photo of a group of campers in white shirts under colourful paper flags"/>
      <polygon points="0,108 348,196 348,202 0,116" fill="var(--brand-blue)"/>
      <polygon points="0,0 82,0 0,112" fill="var(--brand-blue)"/>
    </svg>
    <div class="brand-name">Lantern<br>Cove</div>
    <h2 class="headline">LANGUAGE IMMERSION</h2>
    <p class="subhead">Summer and Break Camps</p>
    <p class="tagline">All the fun of a “traditional” summer camp</p>
    <div class="cta"><svg width="10" height="12" viewBox="0 0 10 12"><polygon points="0,0 10,6 0,12" fill="currentColor"/></svg>SIGN UP</div>
    <div class="site-url">lanterncove-example.org</div>
  </section>

  <section class="banner leaderboard" aria-label="Lantern Cove 468 by 60 banner">
    <svg class="art" viewBox="0 0 651 84" height="98" preserveAspectRatio="none">
      <defs>
        <linearGradient id="board-photo" x1="0" y1="0" x2="1" y2="1">
          <stop offset="0" stop-color="#5a7aa8"/>
          <stop offset="0.4" stop-color="#7fb8a6"/>
          <stop offset="0.75" stop-color="#9a6a44"/>
          <stop offset="1" stop-color="#5e4630"/>
        </linearGradient>
      </defs>
      <polygon points="0,0 201,0 184,84 0,84" fill="url(#board-photo)" role="img" aria-label="Photo of cheering campers in teal shirts in a decorated classroom"/>
      <polygon points="201,0 205,0 188,84 184,84" fill="var(--brand-blue)"/>
      <polygon points="0,44 0,84 66,84" fill="var(--brand-blue)"/>
    </svg>
    <div class="brand-name">Lantern Cove</div>
    <h2 class="headline">LANGUAGE IMMERSION</h2>
    <p class="subhead">Summer and Break Camps</p>
    <p class="tagline">All the fun of a<br>“traditional”<br>summer camp</p>
    <div class="cta"><svg width="8" height="10" viewBox="0 0 10 12"><polygon points="0,0 10,6 0,12" fill="currentColor"/></svg>SIGN UP</div>
    <div class="site-url">lanterncove-example.org</div>
  </section>

</main>
</body>
</html>
```